Creative Website Design for QTDF

Looking for a creative not to corporate design. I have included the brand guidelines which should be followed as well as a sitemap.

You will find a document that has the verbiage and some basic guidelines for the home page.

I have also included the font for headings and logo is uploaded.

The infographics that are included are there to show you some items they used for marketing before in the past.

Looking for a very modern design.

Extended the due date.

Target Market(s)

African American Workers

Industry/Entity Type

Employment Agency

Number of Pages Required

2 page

Requirements
Must have
• a creative feel, following brand guidelines.
Nice to have
• Use of photos, following brand guidelines
Should not have
• Must not be super corporate in feel,

```html
<!DOCTYPE html>
<html lang="en">
<head>
<meta charset="utf-8">
<title>QTDF — Quarter Trade Dignity Forum</title>
<link rel="stylesheet" href="https://fonts.googleapis.com/css2?family=Lato:wght@400;700;900&display=swap">
<style>
:root{
  --red:#c4143b;
  --red-dark:#a80f31;
  --green:#3aa547;
  --ink:#1b1b1b;
  --text:#3a3a3a;
  --muted:#7a7a7a;
  --field:#efefef;
  --footer:#1d1d1d;
  --white:#ffffff;
}
*{box-sizing:border-box;margin:0;padding:0}
html,body{width:1200px;height:4281px;overflow:hidden;background:var(--white)}
body{font-family:'Lato',sans-serif;color:var(--text);position:relative}
.abs{position:absolute}
svg.deco{position:absolute;left:0;width:1200px}

/* header */
.site-header{position:absolute;top:0;left:0;width:1200px;height:83px;background:var(--white);z-index:5}
.brand{position:absolute;left:113px;top:18px;display:flex;align-items:center;gap:10px;font-weight:900;font-size:36px;color:var(--red);letter-spacing:1px}
.brand-dot{width:16px;height:16px;border-radius:50%;background:var(--green)}
.nav{position:absolute;top:31px;left:412px;font-size:15px;color:#333}
.nav a{text-decoration:none;color:#333;position:absolute;white-space:nowrap}
.nav a.active{color:var(--red)}
.nav a.active::after{content:"";position:absolute;left:0;right:0;top:30px;height:3px;background:var(--red)}

/* hero */
.hero-photo{position:absolute;top:83px;left:0;width:1200px;height:700px;background:linear-gradient(120deg,#5b4634 0%,#8a6d4f 35%,#3c3a44 60%,#1f2a44 75%,#8b7a66 100%)}
.hero-text{position:absolute;top:292px;left:122px;width:956px;text-align:center;color:var(--white);font-size:21.5px;font-weight:700;line-height:33px;letter-spacing:.3px;text-shadow:0 2px 6px rgba(0,0,0,.55)}
.play{position:absolute;left:530px;top:431px;width:138px;height:138px;border-radius:50%;border:2px solid rgba(255,255,255,.85)}
.play::after{content:"";position:absolute;left:54px;top:40px;border-left:44px solid var(--white);border-top:28px solid transparent;border-bottom:28px solid transparent}

/* common */
.h2{font-weight:900;font-size:34px;color:var(--ink);letter-spacing:.5px}
.h2 .accent{color:var(--green)}
.btn{position:absolute;display:flex;align-items:center;justify-content:center;border-radius:30px;font-weight:900;font-size:15px;letter-spacing:.5px;text-transform:uppercase;white-space:nowrap}
.btn-red{background:var(--red);color:var(--white);box-shadow:0 4px 8px rgba(0,0,0,.2)}
.btn-outline{border:2px solid var(--red);color:var(--red);background:var(--white)}

/* about */
.about-photo{position:absolute;left:111px;top:822px;width:366px;height:366px;border-radius:50%;border:3px solid var(--green);background:radial-gradient(circle at 50% 40%,#d79a5e,#b3683a 50%,#6b4a33 100%)}
.about-photo-small{position:absolute;left:391px;top:1051px;width:132px;height:132px;border-radius:50%;border:4px solid var(--white);background:radial-gradient(circle at 50% 40%,#9aa3ad,#3c4654 70%);box-shadow:0 2px 6px rgba(0,0,0,.2)}
.about-title{position:absolute;left:600px;top:870px}
.about-copy{position:absolute;left:600px;top:925px;width:485px;font-size:15px;line-height:26px;letter-spacing:.45px;color:#333}

/* our work */
.work-title{position:absolute;left:111px;top:1422px;color:var(--white)}
.work-title .accent{color:var(--green)}
.work-copy{position:absolute;left:111px;top:1475px;width:480px;color:var(--white);font-size:15px;line-height:25.5px;font-weight:700;letter-spacing:.35px}
.work-list{list-style:none;margin-top:15px}
.work-list li{position:relative;padding-left:21px;margin-bottom:12px}
.work-list li::before{content:"";position:absolute;left:2px;top:10px;width:6px;height:6px;border-radius:50%;background:var(--white)}
.btn-dark{background:var(--red-dark);color:var(--white);box-shadow:0 4px 10px rgba(0,0,0,.25)}

/* resources */
.center{position:absolute;left:0;width:1200px;text-align:center}
.res-sub{font-size:19px;color:#222}

/* news */
.news-title{color:var(--ink)}
.card{position:absolute;top:2561px;width:311px;height:334px;background:var(--white);border-radius:4px;overflow:hidden;box-shadow:0 2px 8px rgba(0,0,0,.12)}
.card-media{height:211px}
.card-body{padding:13px 13px 0}
.card-title{font-size:16px;color:var(--ink);font-weight:400;letter-spacing:.2px;margin-top:-1px}
.card-text{font-size:13px;color:var(--muted);line-height:21px;margin-top:6px}
.card-link{display:inline-block;margin-top:5px;font-size:13px;color:var(--red);text-decoration:underline;font-weight:700}

/* join */
.info-row{position:absolute;left:111px;display:flex;gap:30px}
.info-row svg{flex:none}
.info-head{font-weight:900;font-size:18px;color:var(--ink);letter-spacing:.5px}
.info-text{font-size:16px;line-height:24px;color:#222}
.social{position:absolute;top:3601px;width:54px;height:54px;border-radius:50%;background:var(--red)}
.field{position:absolute;background:var(--field);border-radius:3px;box-shadow:0 1px 3px rgba(0,0,0,.12);display:flex;align-items:flex-start;padding:17px 0 0 15px;gap:10px;font-size:15px;color:#777}

/* footer */
.footer-bg{position:absolute;left:0;top:3885px;width:1200px;height:396px;background:linear-gradient(100deg,#151515,#2a2a2a 40%,#1a1a1a)}
.footer-brand{position:absolute;left:136px;top:3970px;display:flex;align-items:center;gap:14px;font-weight:900;font-size:74px;color:var(--white);letter-spacing:2px}
.footer-brand .dot{width:22px;height:22px;border-radius:50%;background:var(--red)}
.f-col{position:absolute;top:3953px;color:var(--white)}
.f-col h3{font-weight:900;font-size:22px;letter-spacing:.5px;margin-bottom:17px}
.f-col a{display:block;font-size:13px;color:#cfcfcf;text-decoration:none;line-height:25px}
.f-rule{position:absolute;left:111px;top:4205px;width:978px;height:1px;background:#555}
.f-bottom{position:absolute;top:4229px;font-size:13px;color:#cfcfcf}
</style>
</head>
<body>

<header class="site-header">
  <div class="brand"><span>QTDF</span><span class="brand-dot"></span></div>
  <nav class="nav">
    <a class="active" style="left:0">HOME</a>
    <a style="left:82px">ABOUT US</a>
    <a style="left:192px">OUR WORK</a>
    <a style="left:311px">RESOURCES</a>
    <a style="left:433px">NEWS</a>
    <a style="left:512px">JOIN US</a>
    <a style="left:605px">CONTACT</a>
  </nav>
</header>

<section class="hero">
  <div class="hero-photo" role="img" aria-label="Smiling professional in a navy suit standing in a bright open-plan office"></div>
  <p class="hero-text">All that we need begins with us. All that our race needs, begins with us. We move forward for ourselves and our people with a joyful militancy that will not be contained. We haven't come this far to not go the distance.</p>
  <div class="play" aria-label="Play video"></div>
  <svg class="deco" style="top:620px" height="170" viewBox="0 0 1200 170">
    <path d="M0,28 Q600,150 1200,40 L1200,170 L0,170 Z" fill="#fff"/>
    <path d="M70,60 Q600,200 1135,60 Q600,150 70,60 Z" fill="var(--red)"/>
  </svg>
</section>

<section class="about">
  <div class="about-photo" role="img" aria-label="Joyful man celebrating in front of a laptop"></div>
  <div class="about-photo-small" role="img" aria-label="Portrait of a smiling businesswoman"></div>
  <h2 class="h2 about-title">ABOUT <span class="accent">US</span></h2>
  <p class="about-copy">Centered at the nexus of racial and economic justice since our founding in 201, Quarter Trade Dignity Forum (QTDF) unites Black workers across employment sectors through organizing, advocacy, and educational programs to build the power needed to free ourselves from systemic racial and economic oppression in workplaces and throughout society.</p>
  <div class="btn btn-red" style="left:600px;top:1102px;width:167px;height:48px">Read More</div>
</section>

<section class="work">
  <svg class="deco" style="top:1240px" height="820" viewBox="0 0 1200 820">
    <defs>
      <clipPath id="workClip"><path d="M0,80 Q600,5 1200,80 L1200,745 Q600,800 0,745 Z"/></clipPath>
      <linearGradient id="workPhoto" x1="0" y1="0" x2="1" y2="1">
        <stop offset="0" stop-color="#e9ecef"/><stop offset=".55" stop-color="#cdd3da"/><stop offset="1" stop-color="#aeb6bf"/>
      </linearGradient>
    </defs>
    <path d="M95,72 Q600,-20 1108,72 Q600,18 95,72 Z" fill="var(--red)"/>
    <g clip-path="url(#workClip)">
      <rect x="0" y="0" width="1200" height="820" fill="var(--red)"/>
      <path d="M800,0 Q600,250 600,420 L600,820 L1200,820 L1200,0 Z" fill="url(#workPhoto)" role="img" aria-label="Young man in a light shirt presenting at a whiteboard"/>
    </g>
    <path d="M70,740 Q600,850 1135,740 Q600,800 70,740 Z" fill="var(--red)"/>
  </svg>
  <h2 class="h2 work-title">OUR <span class="accent">WORK</span></h2>
  <div class="work-copy">
    <p>A radical improvement in the quality of Black life cannot be achieved by simply gaining better access to the labor market for individual Black workers. What is needed is the building of Black workers' collective power. This new approach requires a shift in three ways:</p>
    <ul class="work-list">
      <li>Black worker activism must be focused upon organizing for power and not just delivering services to individuals</li>
      <li>Black worker activism must be focused upon broad community uplift and not just gaining individual achievement</li>
      <li>Black worker activism must be focused upon collective action and not just individual action</li>
    </ul>
  </div>
  <div class="btn btn-dark" style="left:111px;top:1812px;width:167px;height:46px">Read More</div>
</section>

<section class="resources">
  <h2 class="h2 center" style="top:2116px">RESOURCES</h2>
  <p class="center res-sub" style="top:2178px">Are you ready to add your voice in the movement to build Black worker power?</p>
  <div class="btn btn-red" style="left:299px;top:2230px;width:290px;height:47px">Sign the StandTall Pledge</div>
  <div class="btn btn-outline" style="left:610px;top:2230px;width:290px;height:47px">Sign up for Action Alerts</div>
</section>

<section class="news">
  <svg class="deco" style="top:2340px" height="820" viewBox="0 0 1200 820">
    <path d="M95,72 Q600,-20 1108,72 Q600,18 95,72 Z" fill="var(--red)"/>
    <path d="M0,110 Q600,20 1200,110 L1200,700 Q600,780 0,700 Z" fill="var(--green)" role="img" aria-label="Green-tinted portrait of a man in glasses behind the news section"/>
    <path d="M70,735 Q600,845 1135,735 Q600,795 70,735 Z" fill="var(--red)"/>
  </svg>
  <h2 class="h2 center news-title" style="top:2507px">NEWS</h2>
  <article class="card" style="left:111px">
    <div class="card-media" role="img" aria-label="Woman in glasses working on a laptop" style="background:linear-gradient(135deg,#8b6b4d,#c9a987 55%,#6f5843)"></div>
    <div class="card-body"><h3 class="card-title">PERSPICIATIS UNDE OMNISITE</h3><p class="card-text">Uandeomnis iste natus error sit voluptatem accusantium doloremque laudantium.</p><a class="card-link">READ MORE</a></div>
  </article>
  <article class="card" style="left:445px">
    <div class="card-media" role="img" aria-label="Man writing notes at a desk beside a laptop" style="background:linear-gradient(135deg,#e8e2da,#b8a892 55%,#6b5a49)"></div>
    <div class="card-body"><h3 class="card-title">PERSPICIATIS UNDE OMNISITE</h3><p class="card-text">Uandeomnis iste natus error sit voluptatem accusantium doloremque laudantium.</p><a class="card-link">READ MORE</a></div>
  </article>
  <article class="card" style="left:778px">
    <div class="card-media" role="img" aria-label="Smiling businesswoman in a grey blazer in an office corridor" style="background:linear-gradient(135deg,#d9dcdf,#a7adb3 55%,#4d5058)"></div>
    <div class="card-body"><h3 class="card-title">PERSPICIATIS UNDE OMNISITE</h3><p class="card-text">Uandeomnis iste natus error sit voluptatem accusantium doloremque laudantium.</p><a class="card-link">READ MORE</a></div>
  </article>
  <div class="btn btn-red" style="left:517px;top:2937px;width:165px;height:46px">View More</div>
</section>

<section class="join">
  <h2 class="h2 center" style="top:3230px">JOIN <span class="accent" style="color:var(--green)">US</span></h2>

  <div class="info-row" style="top:3340px">
    <svg width="26" height="34" viewBox="0 0 26 34"><path d="M13,1 C6,1 1,6 1,13 C1,22 13,33 13,33 C13,33 25,22 25,13 C25,6 20,1 13,1 Z" fill="var(--red)"/><circle cx="13" cy="13" r="5" fill="#fff"/></svg>
    <p class="info-text" style="margin-left:2px">48 Orchard Row, Fairhaven, Vermont,<br>05743, USA</p>
  </div>
  <div class="info-row" style="top:3417px">
    <svg width="32" height="24" viewBox="0 0 32 24" style="margin-top:8px"><rect x="1" y="1" width="30" height="22" fill="none" stroke="var(--red)" stroke-width="2"/><path d="M1,1 L16,13 L31,1 M1,23 L12,11 M31,23 L20,11" fill="none" stroke="var(--red)" stroke-width="2"/></svg>
    <div><p class="info-head">GENERAL ENQUIRIES:</p><p class="info-text" style="margin-top:4px">info@qtdf.org<br>hello@quartertradeforum.org</p></div>
  </div>
  <div class="info-row" style="top:3522px">
    <svg width="32" height="32" viewBox="0 0 32 32" style="margin-top:6px"><path d="M7,2 L12,9 L9,13 Q12,20 19,23 L23,20 L30,25 L26,30 Q12,30 2,12 Z" fill="none" stroke="var(--red)" stroke-width="2" stroke-linejoin="round"/></svg>
    <div><p class="info-head">PHONE:</p><p class="info-text" style="margin-top:4px">555-014-2290</p></div>
  </div>
  <div class="social" style="left:128px" aria-label="Social profile one"></div>
  <div class="social" style="left:193px" aria-label="Social profile two"></div>
  <div class="social" style="left:257px" aria-label="Social profile three"></div>

  <form>
    <div class="field" style="left:548px;top:3317px;width:256px;height:50px"><svg width="14" height="15" viewBox="0 0 14 15"><circle cx="7" cy="4" r="3.5" fill="var(--red)"/><path d="M0,15 Q0,8 7,8 Q14,8 14,15 Z" fill="var(--red)"/></svg>First Name</div>
    <div class="field" style="left:832px;top:3317px;width:257px;height:50px"><svg width="15" height="15" viewBox="0 0 15 15"><path d="M2,1 L5,1 L6,5 L4,6.5 Q6,10 9,11 L10.5,9 L14,10 L14,13 Q7,15 1,5 Z" fill="var(--red)"/></svg>Phone</div>
    <div class="field" style="left:548px;top:3394px;width:256px;height:50px"><svg width="17" height="13" viewBox="0 0 17 13"><rect width="17" height="13" fill="var(--red)"/><path d="M0,0 L8.5,7 L17,0" fill="none" stroke="#fff" stroke-width="1.5"/></svg>Email</div>
    <div class="field" style="left:832px;top:3394px;width:257px;height:50px"><svg width="17" height="15" viewBox="0 0 17 15"><rect x="1" y="4" width="15" height="10" fill="none" stroke="var(--red)" stroke-width="1.5"/><path d="M8.5,1 L8.5,8" stroke="var(--red)" stroke-width="1.5"/></svg>Zip/Postal Code</div>
    <div class="field" style="left:548px;top:3470px;width:541px;height:157px"><svg width="14" height="14" viewBox="0 0 14 14"><path d="M2,2 L12,12" stroke="var(--red)" stroke-width="2.5" stroke-linecap="round"/></svg>Enter Message</div>
    <div class="btn btn-red" style="left:548px;top:3651px;width:167px;height:49px">Submit</div>
  </form>
</section>

<footer>
  <svg class="deco" style="top:3780px" height="110" viewBox="0 0 1200 110">
    <path d="M95,72 Q600,-20 1108,72 Q600,18 95,72 Z" fill="var(--red)"/>
    <path d="M0,110 Q600,40 1200,110 Z" fill="var(--footer)"/>
  </svg>
  <div class="footer-bg" role="img" aria-label="Dark-toned portrait of a smiling man behind the footer"></div>
  <div class="footer-brand"><span>QTDF</span><span class="dot"></span></div>
  <div class="f-col" style="left:470px"><h3>QUICK LINKS</h3><a>Home</a><a>About Us</a><a>Our Work</a><a>Resources</a><a>News</a><a>Join Us</a><a>Contact</a></div>
  <div class="f-col" style="left:716px"><h3>LINKS</h3><a>FAQ'S</a><a>Terms &amp; Condition</a><a>Privacy Policy</a><a>Sitemap</a></div>
  <div class="f-col" style="left:966px"><h3>SUPPORT</h3><a>Team</a><a>About Us</a><a>Careers</a><a>Our Values</a></div>
  <div class="f-rule"></div>
  <p class="f-bottom" style="left:111px">Copyrights ©2021. All Rights Reserved</p>
  <p class="f-bottom" style="left:880px">Privacy Policy</p>
  <div class="abs" style="left:985px;top:4212px;width:1px;height:40px;background:var(--red)"></div>
  <p class="f-bottom" style="left:1001px">Terms and Use</p>
</footer>

</body>
</html>
```